Collectible Card Trading Company ~ Tidewell and Finch Collectibles

Business card design using the attached images as a reference point. The color pallet is the color choice I prefer. If you have any way of improving on the design that would be appreciated. This will be used as an insert for product shipments as well as at geekfair and other collectible trade shows so it needs to be eye catching and memorable. Anything that you can do to make my business POP with this business card would be appreciated.

Target Market(s)

Collectible card purchasers primarily but all collectors ingeneral

Industry/Entity Type

Retail

Contact Information for Business Card

Details are included on the provided images

Colors

Designer to choose colors to be used in the design.

Requirements
Must have
• Bold design
Nice to have
• N/A
Should not have
• N/A

```html
<!DOCTYPE html>
<html lang="en">
<head>
<meta charset="utf-8">
<title>Tidewell and Finch Collectibles – Business Card</title>
<link rel="stylesheet" href="https://fonts.googleapis.com/css2?family=Merriweather:wght@400;700&family=Roboto+Condensed:wght@400&family=Saira+Condensed:wght@700&family=Exo+2:wght@500&display=swap">
<style>
  :root {
    --backdrop: #9a9293;
    --rust: #7b3a15;
    --rust-dark: #5e2b0e;
    --cream: #eadcb9;
    --cream-edge: #d8c394;
    --ink-brown: #a8622f;
    --white-ink: #f6efe6;
  }
  * { margin: 0; padding: 0; box-sizing: border-box; }
  html, body { width: 1200px; height: 1200px; overflow: hidden; background: var(--backdrop); }
  .canvas { position: relative; width: 1200px; height: 1200px; }

  .card {
    position: absolute; left: 250px; width: 700px; height: 400px;
    box-shadow: 0 10px 24px rgba(0,0,0,.25);
    overflow: hidden;
  }

  /* Back side */
  .card-back { top: 120px; background: var(--rust); color: var(--white-ink); font-family: "Merriweather", serif; }
  .back-band { position: absolute; top: 0; left: 0; width: 100%; height: 34px; background: var(--rust-dark); }
  .shop-line {
    position: absolute; top: 44px; left: 0; width: 100%; text-align: center;
    font-size: 16px; transform: rotate(180deg);
  }
  .web-line {
    position: absolute; right: 22px; top: 50%; font-size: 17px;
    transform: translate(50%, -50%) rotate(90deg); white-space: nowrap;
  }
  .social-lines {
    position: absolute; left: 60px; bottom: 40px; font-size: 16px; line-height: 1.6;
    transform: rotate(-90deg); transform-origin: left bottom; white-space: nowrap;
  }
  .social-lines .posts { font-weight: 700; }
  .person {
    position: absolute; top: 150px; left: 0; width: 100%; text-align: center;
    font-weight: 700; font-size: 26px; line-height: 1.15;
  }
  .contact {
    position: absolute; right: 70px; bottom: 46px; text-align: left;
    font-family: "Roboto Condensed", sans-serif; font-size: 22px; line-height: 1.3;
  }

  /* Front side */
  .card-front { top: 640px; background: var(--cream); border: 6px solid var(--cream-edge); color: var(--ink-brown); }
  .brand-name {
    position: absolute; top: 34px; left: 0; width: 100%; text-align: center;
    font-family: "Saira Condensed", sans-serif; font-weight: 700; font-size: 54px; letter-spacing: 1px;
  }
  .emblem {
    position: absolute; top: 118px; left: 270px; width: 148px; height: 160px;
    border-radius: 46% 46% 40% 40%;
    background: radial-gradient(circle at 50% 45%, #c98d58, var(--ink-brown));
    opacity: .85;
  }
  .est { position: absolute; top: 226px; left: 140px; font-family: "Merriweather", serif; font-weight: 700; font-size: 24px; }
  .year { position: absolute; top: 160px; right: 140px; font-family: "Merriweather", serif; font-weight: 700; font-size: 24px; }
  .tagline {
    position: absolute; bottom: 42px; left: 0; width: 100%; text-align: center;
    font-family: "Exo 2", sans-serif; font-weight: 500; font-size: 36px;
  }
</style>
</head>
<body>
<main class="canvas">
  <section class="card card-back">
    <div class="back-band"></div>
    <p class="shop-line">bids@www.bidhall.com/str/tidewellfinch</p>
    <p class="web-line">www.tidewellfinch.com</p>
    <div class="social-lines">
      <p>photos@tidewellfinch</p>
      <p class="posts">posts@Tidewell_Finch</p>
    </div>
    <p class="person">miles harrow jr.<br>chief collector</p>
    <div class="contact">
      <p>miles@tidewellfinch.com</p>
      <p>cedar bluff, ohio</p>
    </div>
  </section>

  <section class="card card-front">
    <h1 class="brand-name">Tidewell and Finch Collectibles</h1>
    <div class="emblem" role="img" aria-label="Illustration of a roaring big cat head in brown line work"></div>
    <p class="est">est.</p>
    <p class="year">2016</p>
    <p class="tagline">Cards &amp; Collectibles</p>
  </section>
</main>
</body>
</html>
```